Optometry practice sign/banner

Modern design appeal to mix demographic, family friendly. Emphasize the importance of eye exam.
Brigh colors, green,blue, yellow,
Photo of people wearing glasses
4'x8'

" EYE EXAM, CONTACT LENS, ORTHOK, LASIK CONSULTATION, DIABETES RETINAL EXAM
DR. NORA PEL
TALVIN OPTOMETRY " Eyecare for your family"
555.762.4139
MEDICAL, VITALBASE, QRT, BRAVELINK, WALK IN WELCOME"

Target Market(s)

Family, middle age, mix demographic

Colors
33b8a4
fbee3d
cee9f5
9bcb3c

Requirements
Nice to have
• Photo of family wearing glasses.

```html
<!DOCTYPE html>
<html lang="en">
<head>
<meta charset="utf-8">
<title>Talvin Optometry Banner</title>
<link href="https://fonts.googleapis.com/css2?family=Lato:ital,wght@0,300;0,400;0,700;1,300;1,400&display=swap" rel="stylesheet">
<style>
  :root {
    --page: #e6e7e9;
    --panel-top: #f4f5f6;
    --panel-bottom: #ffffff;
    --brand-blue: #2b7fc3;
    --band-blue: #2a7cc0;
    --band-blue-dark: #1f68a8;
    --headline-grey: #6b6b6b;
    --logo-gold: #e3b42b;
    --white: #ffffff;
    --photo-light: #e4e8ec;
    --photo-mid: #cfd6dd;
    --photo-deep: #8fa3b8;
  }
  * { box-sizing: border-box; margin: 0; padding: 0; }
  html, body { width: 1200px; height: 855px; overflow: hidden; background: var(--page); }
  body { position: relative; font-family: "Lato", sans-serif; }

  .banner {
    position: absolute; left: 40px; top: 147px; width: 1120px; height: 560px;
    background: linear-gradient(180deg, var(--panel-top), var(--panel-bottom) 60%);
    overflow: hidden; box-shadow: 0 6px 18px rgba(0,0,0,0.18);
  }
  .banner-shapes { position: absolute; inset: 0; }

  .brand { position: absolute; left: 38px; top: 23px; width: 120px; display: flex; flex-direction: column; align-items: center; gap: 8px; }
  .brand-mark { width: 78px; height: 78px; background: var(--logo-gold); }
  .brand-name { font-weight: 300; font-size: 15px; letter-spacing: 1px; color: var(--headline-grey); text-align: center; line-height: 1.1; }

  .headline {
    position: absolute; left: 185px; top: 47px; width: 232px;
    font-weight: 300; font-size: 29px; line-height: 32px; color: var(--headline-grey); text-transform: uppercase;
  }

  .services { position: absolute; left: 42px; top: 186px; list-style: none; }
  .services li {
    display: flex; align-items: center; gap: 10px;
    font-size: 25px; line-height: 37px; color: var(--brand-blue);
  }
  .services svg { width: 18px; height: 18px; flex: none; }

  .phone { position: absolute; left: 44px; top: 379px; height: 66px; display: flex; align-items: center; gap: 10px; }
  .phone svg { width: 50px; height: 50px; }
  .phone-number { font-weight: 700; font-size: 56px; line-height: 66px; color: var(--brand-blue); letter-spacing: 0.5px; }

  .website {
    position: absolute; left: 50px; top: 458px; font-weight: 400; font-size: 44px;
    color: var(--white); letter-spacing: 0.5px; line-height: 58px;
  }

  .address {
    position: absolute; left: 52px; top: 531px; font-style: italic; font-size: 14px; line-height: 18px; color: var(--brand-blue);
  }
  .social { position: absolute; left: 450px; top: 529px; display: flex; gap: 4px; }
  .social span { width: 22px; height: 22px; background: var(--band-blue); }

  .tagline {
    position: absolute; left: 540px; top: 23px; width: 340px; height: 46px;
    font-style: italic; font-weight: 300; font-size: 27px; color: var(--white);
    display: flex; align-items: center; justify-content: center; letter-spacing: 0.5px;
  }
</style>
</head>
<body>
  <section class="banner">
    <svg class="banner-shapes" viewBox="0 0 1120 560" width="1120" height="560">
      <defs>
        <linearGradient id="photoTone" x1="0" y1="0" x2="1" y2="1">
          <stop offset="0" stop-color="var(--photo-light)"/>
          <stop offset="0.55" stop-color="var(--photo-mid)"/>
          <stop offset="1" stop-color="var(--photo-deep)"/>
        </linearGradient>
      </defs>
      <path role="img" aria-label="Photo of a smiling family of four wearing glasses, sitting together on a sofa"
            d="M560,70 H1120 V560 H600 C560,470 505,380 497,285 C492,200 515,125 560,70 Z"
            fill="url(#photoTone)"/>
      <polygon points="0,458 580,458 608,516 0,516" fill="var(--band-blue)"/>
      <polygon points="580,458 608,516 598,516 572,458" fill="var(--band-blue-dark)"/>
      <polygon points="545,23 880,23 880,69 533,69" fill="var(--band-blue)"/>
    </svg>

    <div class="brand">
      <span class="brand-mark"></span>
      <span class="brand-name">TALVIN OPTOMETRY</span>
    </div>

    <h1 class="headline">Your quality of life is our goal</h1>

    <ul class="services">
      <li><svg viewBox="0 0 18 18"><path d="M2,9 L7,14 L16,4" fill="none" stroke="var(--brand-blue)" stroke-width="2.6"/></svg>Comprehensive Eye Examinations</li>
      <li><svg viewBox="0 0 18 18"><path d="M2,9 L7,14 L16,4" fill="none" stroke="var(--brand-blue)" stroke-width="2.6"/></svg>Contact Lenses</li>
      <li><svg viewBox="0 0 18 18"><path d="M2,9 L7,14 L16,4" fill="none" stroke="var(--brand-blue)" stroke-width="2.6"/></svg>Orthokeratology (OrthoK)</li>
      <li><svg viewBox="0 0 18 18"><path d="M2,9 L7,14 L16,4" fill="none" stroke="var(--brand-blue)" stroke-width="2.6"/></svg>Lasik Consultation</li>
      <li><svg viewBox="0 0 18 18"><path d="M2,9 L7,14 L16,4" fill="none" stroke="var(--brand-blue)" stroke-width="2.6"/></svg>Diabetes Retinal Exam</li>
    </ul>

    <div class="phone">
      <svg viewBox="0 0 52 52" aria-hidden="true">
        <circle cx="26" cy="26" r="23" fill="none" stroke="var(--brand-blue)" stroke-width="3.5"/>
        <path d="M18,14 l5,-2 l4,8 l-4,3 c2,4 4,6 8,8 l3,-4 l8,4 l-2,5 c-10,2 -24,-12 -22,-22 z" fill="var(--brand-blue)"/>
      </svg>
      <span class="phone-number">555.762.4139</span>
    </div>

    <p class="website">www.talvinsee.com</p>

    <p class="address">TALVIN Optometry 4820 Marlow Ave., Fenwick, CA 90217</p>
    <div class="social" aria-hidden="true"><span></span><span></span><span></span><span></span></div>

    <p class="tagline">Eyecare for your family</p>
  </section>
</body>
</html>
```